Poster for Kirtan Music Event

Design (3) 24" x 36" Posters

I have provided a sample a friend did in Australia: ( Picture No. 4 )

Use all the text on sample poster except the replacement changes below.

Replace with the following text as this is for different location:
Replacement Text:

Every Friday Night 7:00pm-8:30pm
Nohea Breath & Movement Loft
752 Wenmore St Paia

Free Kirtan Experience! or Free Event
Madhava Vani Prabhu & Friends

Optional Text:

A evening of music, singing of spiritual mantras, and refreshments

Bring flowers, musical instruments, friends, or just come with an open heart.

Meditate on transcendental sounds that provide rest for the mind & heart"

An evening of music & singing of sacred mantra's

```html
<!DOCTYPE html>
<html lang="en">
<head>
<meta charset="utf-8">
<title>Kirtan Experience – Poster</title>
<link rel="stylesheet" href="https://fonts.googleapis.com/css2?family=Great+Vibes&family=Open+Sans:wght@300;400;600;700&display=swap">
<style>
  :root {
    --night-top: #2a0f45;
    --night-mid: #1a2a9a;
    --night-deep: #0d1a7a;
    --glow: #2f5be0;
    --gold: #f2c23a;
    --gold-light: #ffe68a;
    --gold-soft: rgba(242, 194, 58, 0.26);
    --silhouette: #0b0f4a;
    --silhouette-soft: rgba(11, 15, 74, 0.92);
    --text: #ffffff;
  }
  html, body {
    margin: 0;
    padding: 0;
    overflow: hidden;
    background: #0a0a2a;
  }
  .poster {
    position: relative;
    width: 807px;
    height: 1200px;
    overflow: hidden;
    font-family: "Open Sans", sans-serif;
    color: var(--text);
    background:
      radial-gradient(ellipse 520px 460px at 62% 55%, rgba(47, 91, 224, 0.85), transparent 75%),
      linear-gradient(180deg, var(--night-top) 0%, #241a6a 18%, var(--night-mid) 45%, var(--night-deep) 80%, #0a1466 100%);
  }
  .title-block { margin: 0; }
  .title {
    position: absolute;
    font-family: "Great Vibes", cursive;
    font-weight: 400;
    line-height: 1;
    white-space: nowrap;
    color: var(--gold);
    background: linear-gradient(180deg, var(--gold-light), var(--gold) 70%, #d99a1c);
    -webkit-background-clip: text;
    background-clip: text;
    -webkit-text-fill-color: transparent;
  }
  .title__first { left: 62px; top: 82px; font-size: 130px; }
  .title__second { left: 112px; top: 160px; font-size: 172px; }

  .lotus-art {
    position: absolute;
    left: -180px;
    top: 370px;
    width: 600px;
    height: 830px;
    background: radial-gradient(closest-side, var(--gold-soft), rgba(242, 194, 58, 0.12) 55%, rgba(242, 194, 58, 0) 100%);
  }
  .meditator-art {
    position: absolute;
    left: -60px;
    top: 520px;
    width: 330px;
    height: 460px;
    background: radial-gradient(closest-side, var(--silhouette) 0%, var(--silhouette-soft) 55%, rgba(11, 15, 74, 0) 100%);
  }
  .musicians-art {
    position: absolute;
    left: 400px;
    top: 770px;
    width: 370px;
    height: 520px;
    background: radial-gradient(closest-side, var(--silhouette-soft) 0%, rgba(11, 15, 74, 0.75) 50%, rgba(11, 15, 74, 0) 100%);
  }

  .info {
    position: absolute;
    right: 66px;
    margin: 0;
    text-align: right;
  }
  .headline {
    top: 395px;
    font-size: 28px;
    font-weight: 700;
    line-height: 34px;
  }
  .detail {
    font-size: 19.5px;
    font-weight: 400;
    line-height: 22px;
    letter-spacing: 0.2px;
  }
  .detail--evening { top: 510px; }
  .detail--bring { top: 605px; }
  .detail--mantras { top: 696px; }

  .schedule {
    top: 927px;
    right: 36px;
  }
  .schedule__day { display: block; font-size: 32px; font-weight: 600; line-height: 40px; }
  .schedule__time { display: block; font-size: 28px; font-weight: 300; line-height: 40px; margin-top: 10px; }
  .schedule__venue { display: block; font-size: 26px; font-weight: 600; line-height: 38px; margin-top: 14px; }
  .schedule__address { display: block; font-size: 26px; font-weight: 600; line-height: 38px; }
</style>
</head>
<body>
<main class="poster">
  <div class="lotus-art" role="img" aria-label="Large golden lotus flower outline"></div>
  <div class="meditator-art" role="img" aria-label="Silhouette of a person seated in meditation"></div>
  <div class="musicians-art" role="img" aria-label="Silhouettes of a flute player and a guitarist"></div>

  <h1 class="title-block">
    <span class="title title__first">Kirtan</span>
    <span class="title title__second">Experience</span>
  </h1>

  <h2 class="info headline">Free Kirtan Experience!<br>Madhava Vani Prabhu &amp; Friends</h2>

  <p class="info detail detail--evening">A evening of music, mantra,<br>refreshments and spiritual discourse.</p>
  <p class="info detail detail--bring">Bring flowers, musical instruments,<br>friends, or just come with<br>an open heart.</p>
  <p class="info detail detail--mantras">An evening of music &amp; singing<br>of sacred mantra's</p>

  <p class="info schedule">
    <span class="schedule__day">Every Friday Night</span>
    <span class="schedule__time">7:00pm-8:30pm</span>
    <span class="schedule__venue">Nohea Breath &amp; Movement Loft</span>
    <span class="schedule__address">752 Wenmore St Paia</span>
  </p>
</main>
</body>
</html>
```